Electrical Engineering Business Card Design

I need a business card design for an engineering consulting company based in Orlando, FL. I have had a logo created which the files are attached. We work primarily in the theme park and entertainment market sector but do projects in all market sectors. We have been serving Central Florida since 1994 and continue to strive to serve our clients and provide outstanding designs.
Theme Park

```html
<!DOCTYPE html>
<html lang="en">
<head>
<meta charset="utf-8">
<title>Voltline Associates – Business Card</title>
<link rel="stylesheet" href="https://fonts.googleapis.com/css2?family=Oswald:wght@500;700&family=Open+Sans:wght@400;700&display=swap">
<style>
  :root {
    --brand-green: #8bc157;
    --paper: #ffffff;
    --ink: #1f1f1f;
    --backdrop: #ecebe7;
  }
  html, body {
    margin: 0;
    padding: 0;
    width: 1118px;
    height: 1200px;
    overflow: hidden;
    background: var(--backdrop);
  }
  .canvas {
    display: block;
    width: 1118px;
    height: 1200px;
  }
  .card-front__panel, .card-back__band { fill: var(--brand-green); }
  .card-front__band { fill: var(--paper); }
  .brand-name {
    font-family: "Oswald", sans-serif;
    font-weight: 700;
    font-size: 150px;
    fill: var(--paper);
    letter-spacing: 4px;
  }
  .card-back__outline {
    fill: var(--paper);
    stroke: var(--brand-green);
    stroke-width: 6;
  }
  .company-name {
    font-family: "Oswald", sans-serif;
    font-weight: 500;
    font-size: 44px;
    fill: var(--ink);
  }
  .company-location {
    font-family: "Open Sans", sans-serif;
    font-weight: 700;
    font-size: 17px;
    letter-spacing: 5px;
    fill: var(--ink);
  }
  .address {
    font-family: "Open Sans", sans-serif;
    font-weight: 700;
    font-size: 27px;
    fill: var(--ink);
  }
  .contact {
    font-family: "Open Sans", sans-serif;
    font-weight: 400;
    font-size: 26px;
    fill: var(--paper);
  }
  .fax {
    font-family: "Open Sans", sans-serif;
    font-weight: 400;
    font-size: 19px;
    fill: var(--brand-green);
  }
</style>
</head>
<body>
<svg class="canvas" viewBox="0 0 1118 1200" xmlns="http://www.w3.org/2000/svg">
  <g class="card-front">
    <polygon class="card-front__panel" points="154,143 751,143 918,304 918,540 154,540"/>
    <rect class="card-front__band" x="154" y="429" width="764" height="45"/>
    <text class="brand-name" x="520" y="395" text-anchor="middle">VOLTLINE</text>
  </g>

  <g class="card-back">
    <polygon class="card-back__outline" points="154,639 734,639 911,885 911,1041 154,1041"/>
    <rect class="card-back__band" x="157" y="934" width="751" height="41"/>
    <text class="company-name" x="192" y="736">Voltline Associates, P.A.</text>
    <text class="company-location" x="243" y="776">ORLANDO, FLORIDA</text>
    <text class="address" x="195" y="853">PO Box 480217</text>
    <text class="address" x="195" y="895">Orlando, FL 32801</text>
    <text class="contact" x="195" y="964">voltline.dan@example.com</text>
    <text class="contact" x="592" y="964">407-555-0142</text>
    <text class="fax" x="593" y="1008">fax: 407-555-0187</text>
  </g>
</svg>
</body>
</html>
```